Diesel Trailer Manufacturer Website Design

We are working with a Trailer Manufacturer in Texas. They provide custom-made trailers for diesel trucks throughout the US.
Some sites to use for content/competitors:
www.quillontrailer.com
https://velmortrailers.com
http://www.dunsworthcustomtrailers.com/
https://www.pelhamtrailer.com
https://www.haulzenith.com
Thank you for taking the time to consider designing a website for us. We are web developers based in Stockton, CA, USA. Most of our projects go through the same process. Understanding this process may help you win a project with us. We custom-code all of our websites in-house. We don’t have any requirements as to what tools you use for your design, but we ask that you follow these guidelines.
IMAGES:
If you use any images or icons in the design, we ask that you have a link to the asset so we can purchase the image/icon. Most of the designs we submit do not have the customer’s images on them unless they have some great images. Be creative; show us the feeling you are trying to portray with your image choices. Use any royalty-free site you choose. We subscribe to Vornix and mainly use their images, but we can purchase images outside of Vornix. PLEASE NOTE: we will not submit designs to clients with watermarks on the images.
FONTS:
We ask that you identify the fonts you’re using in the design. This can be done in a message if you want. We typically use Tellura Fonts and Vornix Fonts.
CONTENT:
We're always open to different content and ideas. We often submit designs with stock images so the client can see our vision. We typically take pictures after the website launch to use their images with our vision. Lorem Ipsum is fine for paragraphs, but we ask that you make the Headers with correct English. We want to be able to show the vision and identify the sections of the website.
INSPIRATION:
We typically add a couple of links in the brief of websites we like to help you get started in your design.
REVISIONS:
We do not often ask for revisions of the designs unless we see something in the design that may not appeal to the client. If there are slight changes that we want to make, we do that in the development process.
FEEDBACK:
We rarely give feedback on designs during the design process. We are working on many website projects and do not have the time to provide feedback. We usually respond if your request is well thought out and asks specific questions, but a note asking “feedback, please” usually goes unanswered.

```html
<!DOCTYPE html>
<html lang="en">
<head>
<meta charset="utf-8">
<title>Ridgeback Trailers</title>
<link href="https://fonts.googleapis.com/css2?family=Open+Sans:wght@400;600;700;800&family=Oxygen:wght@400;700&family=Oswald:wght@500&family=Poppins:wght@400;600&display=swap" rel="stylesheet">
<style>
:root{
  --red:#a01208;
  --red-dark:#8a0f06;
  --ink:#111;
  --grey-text:#8a8a8a;
  --body-text:#222;
  --dark:#1c1c1c;
  --black:#0b0b0b;
  --white:#fff;
}
*{box-sizing:border-box;margin:0;padding:0}
html,body{width:1200px;height:3993px;overflow:hidden}
body{position:relative;background:var(--white);font-family:"Oxygen",sans-serif;color:var(--body-text)}
.abs{position:absolute}
.btn{position:absolute;display:flex;align-items:center;justify-content:center;background:var(--red);color:var(--white);border-radius:20px;font-family:"Open Sans",sans-serif;font-weight:600;font-size:14px;text-transform:uppercase}

/* hero */
.hero{position:absolute;left:0;top:0;width:1200px;height:797px;background:linear-gradient(180deg,#5d6a72 0%,#6b7366 30%,#4c5a3a 55%,#2f4626 100%)}
.hero-shade{position:absolute;inset:0;background:rgba(0,0,0,.38)}
.brand{position:absolute;font-family:"Oxygen",sans-serif;font-weight:700;letter-spacing:1px;color:var(--white)}
.nav{position:absolute;left:470px;top:40px;display:flex;gap:28px;font-family:"Oswald",sans-serif;font-weight:500;font-size:15px;color:var(--white)}
.nav .active{color:#d8231a}
.hero-title{position:absolute;left:0;width:1200px;top:272px;text-align:center;color:var(--white);font-family:"Open Sans",sans-serif;font-weight:800;font-size:52px;line-height:53px;text-transform:uppercase}
.hero-sub{position:absolute;left:0;width:1200px;top:451px;text-align:center;color:var(--white);font-family:"Open Sans",sans-serif;font-size:14px;line-height:23px}

/* section headings */
.sec-title{position:absolute;font-family:"Oxygen",sans-serif;font-weight:700;font-size:34px;text-transform:uppercase;color:var(--red)}
.sec-title .muted{color:var(--grey-text)}
.para{position:absolute;font-size:14px;line-height:23px}

/* photo placeholders */
.photo{position:absolute;background:linear-gradient(180deg,#c8d4de 0%,#aebcc4 40%,#6f8a55 70%,#4f6b38 100%)}
.photo.warm{background:linear-gradient(180deg,#b9c9d8 0%,#c9b79a 55%,#9c8666 100%)}
.photo.dark{background:linear-gradient(180deg,#d8dadc 0%,#7c8084 45%,#2a2c2e 100%)}
.photo.red{background:linear-gradient(180deg,#e6e3dc 0%,#c44a3e 50%,#8f8a80 100%)}
.round{border-radius:50%}
.crescent{position:absolute;border-radius:50%;background:var(--red)}

.grey-band{position:absolute;left:0;width:1200px;background:linear-gradient(180deg,#f4f4f4 0%,#d0d0d0 100%)}
.type-label{position:absolute;width:200px;text-align:center;font-weight:700;font-size:14px;text-transform:uppercase;color:#333}
.type-ring{position:absolute;width:144px;height:144px;border-radius:50%;border:4px solid var(--red);overflow:hidden}
.type-ring .photo{inset:0}
.arrow{position:absolute}

.tile{border-radius:12px}

/* contact */
.contact{position:absolute;left:0;top:3285px;width:1200px;height:475px;background:linear-gradient(180deg,#242424,#161616)}
.map{position:absolute;left:189px;top:3400px;width:374px;height:265px;background:linear-gradient(135deg,#e8e4da,#d6dccc 60%,#cfd6e0)}
.field{position:absolute;left:609px;width:373px;height:55px;border:2px solid #cfcfcf;color:#bdbdbd;font-family:"Poppins",sans-serif;font-size:15px;padding:0 20px;display:flex;align-items:center}
.field.select{justify-content:space-between;color:var(--white)}
.send{position:absolute;left:609px;top:3639px;width:373px;height:44px;border-radius:22px;background:var(--red);color:var(--white);font-family:"Poppins",sans-serif;font-weight:600;font-size:15px;letter-spacing:2px;display:flex;align-items:center;justify-content:center}

.footer{position:absolute;left:0;top:3760px;width:1200px;height:233px;background:var(--black)}
.social{position:absolute;top:3940px;width:25px;height:25px;border-radius:50%;background:var(--red)}
</style>
</head>
<body>

<!-- Hero -->
<section class="hero" role="img" aria-label="Yellow semi truck hauling heavy earthmoving equipment on a lowboy trailer through green fields">
  <div class="hero-shade"></div>
</section>
<div class="brand" style="left:86px;top:44px;display:flex;align-items:center;gap:8px;font-size:20px">
  <span style="width:18px;height:18px;border-radius:50%;background:var(--red);display:inline-block"></span>RIDGEBACK
</div>
<nav class="nav">
  <span class="active">Home</span><span>About</span><span>Solutions</span><span>Gallery</span><span>Contact Us</span>
</nav>
<div class="btn" style="left:995px;top:32px;width:148px;height:38px;font-size:15px;text-transform:none;font-weight:700;gap:6px">
  <svg width="16" height="16" viewBox="0 0 16 16"><path d="M3 9V7a5 5 0 0 1 10 0v2" fill="none" stroke="#fff" stroke-width="2"/><rect x="1.5" y="8" width="3" height="5" rx="1" fill="#fff"/><rect x="11.5" y="8" width="3" height="5" rx="1" fill="#fff"/></svg>
  Let's Talk
</div>
<h1 class="hero-title">World-wide leader in<br>manufacturing quality<br>trailers</h1>
<p class="hero-sub">Lorem ipsum dolor sit amet, consectetur adipiscing elit.<br>Ut elit tellus, luctus nec ullamcorper mattis, pulvinar dapibus leo.</p>
<div class="btn" style="left:520px;top:516px;width:177px;height:34px;font-size:13px">Browser Trailers</div>

<!-- About -->
<span class="abs" style="left:141px;top:985px;width:28px;height:28px;border-radius:50%;background:var(--red)"></span>
<h2 class="sec-title" style="left:133px;top:1036px"><span class="muted">About</span> Ridgeback</h2>
<p class="para" style="left:133px;top:1111px;width:440px">Lorem ipsum dolor sit amet, consectetur adipiscing elit. Ut elit tellus, luctus nec ullamcorper mattis, pulvinar dapibus.</p>
<p class="para" style="left:133px;top:1189px;width:440px">Lorem ipsum dolor sit amet, consectetur adipiscing elit. Ut elit tellus, luctus nec ullamcorper mattis, pulvinar dapibus.</p>
<div class="btn" style="left:133px;top:1267px;width:177px;height:37px;font-size:13px">Find your trailer</div>
<div class="crescent" style="left:658px;top:938px;width:422px;height:428px"></div>
<div class="photo round" style="left:652px;top:940px;width:408px;height:408px" role="img" aria-label="Purple multi-axle lowboy trailer parked on a road under power lines"></div>

<!-- Trailer types -->
<section class="grey-band" style="top:1499px;height:539px"></section>
<h2 class="sec-title" style="left:0;width:1170px;text-align:center;top:1605px"><span class="muted">Our</span> Trailer Types</h2>
<p class="para" style="left:240px;width:700px;top:1681px;text-align:center;font-size:14px">Lorem ipsum dolor sit amet, consectetur adipiscing elit. Ut elit tellus, luctus nec ullamcorper mattis, pulvinar dapibus.</p>
<svg class="arrow" style="left:48px;top:1832px" width="22" height="30" viewBox="0 0 22 30"><path d="M17 3 5 15l12 12" fill="none" stroke="var(--red)" stroke-width="5"/></svg>
<svg class="arrow" style="left:1128px;top:1838px" width="22" height="30" viewBox="0 0 22 30"><path d="M5 3l12 12L5 27" fill="none" stroke="var(--red)" stroke-width="5"/></svg>
<div class="type-ring" style="left:134px;top:1770px"><div class="photo dark" role="img" aria-label="Black agricultural dump trailer"></div></div>
<div class="type-ring" style="left:400px;top:1770px"><div class="photo dark" role="img" aria-label="Flatbed trailer deck"></div></div>
<div class="type-ring" style="left:666px;top:1770px"><div class="photo" role="img" aria-label="Materials hauling lowboy trailer"></div></div>
<div class="type-ring" style="left:933px;top:1770px"><div class="photo dark" role="img" aria-label="Specialised extendable trailer"></div></div>
<div class="type-label" style="left:109px;top:1936px">Agricultural</div>
<div class="type-label" style="left:376px;top:1936px">Flatbed</div>
<div class="type-label" style="left:642px;top:1936px">Materials Hauling</div>
<div class="type-label" style="left:909px;top:1936px">Specialised</div>

<!-- Gallery -->
<h2 class="sec-title" style="left:0;width:1220px;text-align:center;top:2108px"><span class="muted">Photo</span> Gallery</h2>
<div class="photo tile" style="left:76px;top:2182px;width:273px;height:180px" role="img" aria-label="Truck hauling equipment across fields"></div>
<div class="photo tile warm" style="left:359px;top:2182px;width:284px;height:180px" role="img" aria-label="Crane loading oversize cargo onto trailer"></div>
<div class="photo tile red" style="left:653px;top:2182px;width:241px;height:180px" role="img" aria-label="Red tipping dump trailer"></div>
<div class="photo tile warm" style="left:906px;top:2182px;width:234px;height:180px" role="img" aria-label="Scraper on trailer in desert"></div>
<div class="photo tile dark" style="left:76px;top:2372px;width:273px;height:171px" role="img" aria-label="Black triple-axle dump trailer"></div>
<div class="photo tile dark" style="left:359px;top:2372px;width:229px;height:171px" role="img" aria-label="Flatbed trailer with ramps"></div>
<div class="photo tile warm" style="left:600px;top:2372px;width:222px;height:171px" role="img" aria-label="Earthmover loaded on trailer"></div>
<div class="photo tile red" style="left:836px;top:2372px;width:304px;height:171px" role="img" aria-label="Bulldozer on red lowboy trailer"></div>

<!-- Financing -->
<section class="grey-band" style="top:2630px;height:655px"></section>
<h2 class="abs" style="left:189px;top:2800px;font-family:'Open Sans',sans-serif;font-weight:800;font-size:50px;line-height:50px;color:var(--ink)">100%<br>EQUIPMENT<br>FINANCING</h2>
<p class="para" style="left:189px;top:2969px;text-transform:uppercase;font-family:'Open Sans',sans-serif">Financing solutions to match your business<br>needs</p>
<div class="btn" style="left:188px;top:3033px;width:147px;height:37px;font-size:13px;gap:6px">Get Started
  <svg width="12" height="8" viewBox="0 0 12 8"><path d="M1 1l5 5 5-5" fill="none" stroke="#fff" stroke-width="2.5"/></svg>
</div>
<div class="crescent" style="left:640px;top:2783px;width:325px;height:327px"></div>
<div class="photo round" style="left:637px;top:2784px;width:310px;height:310px" role="img" aria-label="Purple lowboy trailer parked beside trees"></div>

<!-- Contact -->
<section class="contact" role="img" aria-label="Dimmed background of a trailer workshop"></section>
<div class="map" role="img" aria-label="Location map"></div>
<div class="field" style="top:3400px">Your Name</div>
<div class="field" style="top:3480px">Your email</div>
<div class="field select" style="top:3559px">workshop 1
  <svg width="10" height="6" viewBox="0 0 10 6"><path d="M0 0h10L5 6z" fill="#fff"/></svg>
</div>
<div class="send">Send</div>

<!-- Footer -->
<footer class="footer"></footer>
<div class="brand" style="left:0;width:1200px;top:3842px;text-align:center;font-size:32px;display:flex;justify-content:center;align-items:center;gap:12px">
  <span style="width:26px;height:26px;border-radius:50%;background:var(--red);display:inline-block"></span>RIDGEBACK
</div>
<span class="social" style="left:551px"></span>
<span class="social" style="left:597px"></span>
<span class="social" style="left:643px"></span>

</body>
</html>
```